Escape Room Flyer Design - Start up. A5

Flyer is for letterbox drops to get interest and let people know that our business exists and to a lesser extent what an escape room is. We have 1 room (the miller's ghosts) and a second room coming soon (Morvin's Vault). I have attached our logo and 2 flyers that I have seen in the past that I really like the design of.
Whether you are having a night out with friends or family, celebrating a special event, planning a team-building activity, or simply wanting a diversion from the doldrums of your workweek, The Lock Box will provide you an unforgettable live-action gaming experience.

Target Market(s)

18-25

Industry/Entity Type

Entertainment

Requirements
Must have
• Logo. Phone number 0417 582 391. Website. www.thelockboxharbour.example
Bookings essential.
Nice to have
• Mystery, a little bit on the darker side than bright colourful and blocky.
"Many Will Enter…Few Will Escape" tag line
60 minute game. Team work. 2-6 players. All ages.
Should not have
• Cartoons, characters, people

```html
<!DOCTYPE html>
<html lang="en">
<head>
<meta charset="utf-8">
<title>The Lock Box – Escape Room Flyer</title>
<link href="https://fonts.googleapis.com/css2?family=Bebas+Neue&family=Montserrat:wght@300;400;600&display=swap" rel="stylesheet">
<style>
  :root {
    --page: #e6e6e6;
    --ink-dark: #0f0d0c;
    --ink-mid: #2b241e;
    --gold: #e9b95c;
    --gold-deep: #b7803a;
    --bronze: #8a5a2b;
    --white: #f3f0ea;
    --glow: #f0a63a;
    --rule: #8d8479;
  }
  * { box-sizing: border-box; margin: 0; padding: 0; }
  html, body { width: 907px; height: 1200px; overflow: hidden; background: var(--page); }
  .flyer {
    position: absolute; left: 124px; top: 134px; width: 660px; height: 933px;
    background: radial-gradient(ellipse at 35% 55%, #3a3028 0%, var(--ink-mid) 35%, var(--ink-dark) 85%);
    overflow: hidden; color: var(--white);
    font-family: "Montserrat", Arial, sans-serif;
  }
  .rays { position: absolute; left: 0; top: 300px; width: 660px; height: 560px; }
  .headline {
    position: absolute; left: 40px; top: 112px;
    font-family: "Bebas Neue", Impact, sans-serif; font-size: 60px; line-height: 0.95;
    color: var(--gold); letter-spacing: 1px; font-weight: 400;
  }
  .rule { position: absolute; left: 0; top: 240px; width: 410px; height: 1px; background: var(--rule); }
  .rooms { position: absolute; left: 40px; top: 266px; font-size: 19px; font-weight: 300; color: var(--white); }
  .brand {
    position: absolute; left: 430px; top: 96px; width: 190px;
    display: flex; flex-direction: column; align-items: center; gap: 12px;
  }
  .brand-mark { width: 34px; height: 34px; border-radius: 50%; background: var(--gold-deep); }
  .brand-name {
    font-family: "Bebas Neue", Impact, sans-serif; font-size: 44px; color: var(--gold);
    letter-spacing: 1px; white-space: nowrap;
  }
  .hero-art {
    position: absolute; left: 30px; top: 440px; width: 300px; height: 320px;
    background: radial-gradient(circle at 50% 42%, #f0a63a 0%, #b7803a 14%, #4a3626 42%, #1d1815 75%);
    border-radius: 6px;
  }
  .features { position: absolute; left: 470px; top: 330px; width: 150px; list-style: none; }
  .feature { display: flex; flex-direction: column; align-items: center; margin-bottom: 26px; }
  .feature svg { width: 78px; height: 86px; }
  .feature-label {
    margin-top: 6px; font-size: 15px; font-weight: 600; color: var(--gold);
    text-align: center; line-height: 1.2; text-transform: uppercase;
  }
  .contact {
    position: absolute; left: 40px; top: 806px; width: 600px; height: 70px;
    font-size: 15px; font-style: normal; color: var(--gold);
  }
  .contact-row { position: absolute; display: flex; align-items: center; gap: 10px; white-space: nowrap; }
  .contact-row svg { width: 18px; height: 18px; flex: none; }
  .contact-email { left: 200px; top: 0; }
  .contact-web { left: 170px; top: 30px; }
  .contact-phone { left: 0; top: 36px; font-size: 16px; }
  .bookings {
    position: absolute; left: 0; top: 2px;
    font-size: 13px; font-weight: 600; letter-spacing: 1px; text-transform: uppercase;
    color: var(--white);
  }
</style>
</head>
<body>
<main class="flyer">
  <svg class="rays" viewBox="0 0 660 560" aria-hidden="true">
    <defs>
      <linearGradient id="ray" x1="0" y1="0" x2="1" y2="0">
        <stop offset="0" stop-color="#c9a77a" stop-opacity="0.25"/>
        <stop offset="1" stop-color="#c9a77a" stop-opacity="0"/>
      </linearGradient>
    </defs>
    <polygon points="180,290 660,60 660,200" fill="url(#ray)"/>
    <polygon points="180,290 520,0 600,0" fill="url(#ray)"/>
    <polygon points="180,290 660,380 660,480" fill="url(#ray)" opacity="0.6"/>
  </svg>

  <h1 class="headline">Many will enter…<br>Few will escape</h1>
  <div class="rule"></div>
  <p class="rooms">The Miller's Ghosts | Morvin's Vault</p>

  <div class="brand">
    <span class="brand-mark"></span>
    <span class="brand-name">The Lock Box</span>
  </div>

  <div class="hero-art" role="img" aria-label="Illustration of a glowing keyhole set inside nested golden hexagon frames"></div>

  <ul class="features">
    <li class="feature">
      <svg viewBox="0 0 78 86" aria-hidden="true">
        <polygon points="39,2 76,22 76,64 39,84 2,64 2,22" fill="none" stroke="var(--gold-deep)" stroke-width="2"/>
        <g fill="none" stroke="var(--gold)" stroke-width="2">
          <circle cx="39" cy="36" r="5"/><path d="M29,54 q10,-14 20,0"/>
          <circle cx="25" cy="40" r="4"/><path d="M17,55 q8,-11 16,0"/>
          <circle cx="53" cy="40" r="4"/><path d="M45,55 q8,-11 16,0"/>
        </g>
      </svg>
      <span class="feature-label">2 to 6 players</span>
    </li>
    <li class="feature">
      <svg viewBox="0 0 78 86" aria-hidden="true">
        <polygon points="39,2 76,22 76,64 39,84 2,64 2,22" fill="none" stroke="var(--gold-deep)" stroke-width="2"/>
        <g fill="none" stroke="var(--gold)" stroke-width="2">
          <circle cx="30" cy="32" r="6"/><path d="M30,38 v22 M30,52 h6 M30,58 h5"/>
          <circle cx="52" cy="48" r="5"/><path d="M47,52 l-12,10 M39,59 l3,3"/>
        </g>
      </svg>
      <span class="feature-label">60 minutes<br>of game</span>
    </li>
    <li class="feature">
      <svg viewBox="0 0 78 86" role="img" aria-label="Hexagon badge holding a small dragon emblem">
        <polygon points="39,2 76,22 76,64 39,84 2,64 2,22" fill="none" stroke="var(--gold-deep)" stroke-width="2"/>
        <polygon points="39,22 58,33 58,53 39,64 20,53 20,33" fill="var(--bronze)" opacity="0.5"/>
      </svg>
      <span class="feature-label">Tons of<br>adventure</span>
    </li>
  </ul>

  <address class="contact">
    <span class="bookings">Bookings essential</span>
    <span class="contact-row contact-email">
      <svg viewBox="0 0 18 18" aria-hidden="true"><rect x="1" y="4" width="16" height="11" fill="var(--gold)"/><path d="M1,4 L9,11 L17,4" fill="none" stroke="#1a1512" stroke-width="1.5"/></svg>
      gamemaster@thelockboxharbour.example
    </span>
    <span class="contact-row contact-web">
      <svg viewBox="0 0 18 18" aria-hidden="true"><g fill="none" stroke="var(--gold)" stroke-width="1.4"><circle cx="9" cy="9" r="7"/><ellipse cx="9" cy="9" rx="3" ry="7"/><path d="M2,9 h14"/></g></svg>
      www.thelockboxharbour.example
    </span>
    <span class="contact-row contact-phone">
      <svg viewBox="0 0 18 18" aria-hidden="true"><rect x="0" y="0" width="18" height="18" rx="3" fill="var(--gold)"/><path d="M5,4 l2,0 l1,3 l-1.5,1 q1,2.5 3.5,3.5 l1,-1.5 l3,1 l0,2 q-6,1 -9,-7 z" fill="#1a1512"/></svg>
      0417 582 391
    </span>
  </address>
</main>
</body>
</html>
```